Web Site Design

We need to design the whole web site for our small start up. We sell hospitality and culinary art internships abroad. I did my own design with WIX which is horrible meanwhile I started with my business. You can see it www.brindle-passage.org I will need you to create a new and attractive web site and to leave it working on wix. The internship destinations are United Arab Emirates, Thailand, China, Spain, Brazil and maybe leave a couple of pages for future destinations.You could also get other ideas of other sites that do internships.

Target Market(s)

Students and recent graduates of hospitality and culinary art majors

Industry/Entity Type

Education

Number of Pages Required

5+ page

Requirements
Must have
• Addittional to our program destinations, or to the pages in the current site. The website must contain a page for Universities or Hotels who require our service

```html
<!DOCTYPE html>
<html lang="en">
<head>
<meta charset="utf-8">
<title>Brindle Passage – Hospitality Internships</title>
<link href="https://fonts.googleapis.com/css2?family=Noticia+Text:wght@400;700&family=PT+Sans:wght@400;700&display=swap" rel="stylesheet">
<style>
:root{
  --teal:#24807f;
  --teal-dark:#1d6a69;
  --orange:#f5aa42;
  --ink:#1c1c1c;
  --grey:#8a8a8a;
  --line:#c9c9c9;
  --footer:#23262f;
  --footer-base:#16181d;
  --white:#ffffff;
}
*{margin:0;padding:0;box-sizing:border-box}
html,body{width:708px;height:1200px;overflow:hidden;background:var(--white)}
body{position:relative;font-family:"PT Sans",sans-serif;color:var(--ink)}
.abs{position:absolute}

/* top bar */
.topbar{left:0;top:0;width:708px;height:23px;border-bottom:1px solid #e2e2e2}
.topbar .item{top:0;height:23px;display:flex;align-items:center;gap:5px;padding:0 8px;font-size:6px;color:var(--grey);border-left:1px solid #e2e2e2}
.topbar .item:last-child{border-right:1px solid #e2e2e2}

/* header */
.header{left:0;top:23px;width:708px;height:45px;border-bottom:2px solid var(--orange);background:var(--white)}
.brand{display:flex;align-items:center;gap:6px;font-family:"Noticia Text",serif;font-size:14px;color:var(--teal);white-space:nowrap}
.brand .dot{width:22px;height:22px;border-radius:50%;border:2px solid var(--teal)}
.nav a{position:absolute;top:0;height:43px;line-height:43px;font-size:7px;font-weight:700;color:var(--ink);text-decoration:none;transform:translateX(-50%);white-space:nowrap}
.nav a.active{background:var(--teal);color:var(--white);width:29px;text-align:center;transform:none}
.nav span{position:absolute;top:0;line-height:43px;font-size:7px;color:var(--ink)}

/* hero */
.hero{left:0;top:68px;width:708px;height:342px;background:linear-gradient(180deg,#3d4f62 0%,#6b7a85 35%,#7a5a4a 60%,#4f6a3a 85%,#3e5a2c 100%)}
.hero-title{color:var(--white);font-family:"Noticia Text",serif;font-weight:700;white-space:nowrap}
.cta{left:534px;top:282px;width:78px;height:28px;background:var(--white);color:var(--teal);font-size:6.5px;font-weight:700;display:flex;align-items:center;justify-content:center;letter-spacing:.3px}
.tagline{right:96px;top:321px;font-size:6.5px;font-weight:700;color:var(--white)}

/* program band */
.band{left:0;top:410px;width:708px;height:72px;background:var(--orange);text-align:center}
.band h2{font-family:"Noticia Text",serif;font-size:16px;margin-top:15px}
.band p{font-size:8.5px;font-weight:700;text-decoration:underline;margin-top:4px}

/* form */
.contact{left:0;top:482px;width:708px;height:266px;background:linear-gradient(180deg,#f8f8f8,#e9e9e9)}
.lead{width:708px;top:34px;text-align:center;font-family:"Noticia Text",serif;font-size:13.5px;line-height:21px}
.field{font-size:6px;color:var(--grey);border-bottom:1px solid #bfbfbf;height:16px}
.send{top:200px;width:708px;text-align:center;font-size:7px;font-weight:700}
.resume{top:218px;width:708px;text-align:center;font-family:"Noticia Text",serif;font-size:8.5px;text-decoration:underline}

/* destinations */
.dest-title{left:94px;top:789px;font-family:"Noticia Text",serif;font-size:13.5px;font-weight:400;color:var(--teal-dark)}
.card{top:847px;width:135px;height:148px;background:var(--white);border:1px solid #dcdcdc;text-align:center}
.card h3{margin-top:62px;font-size:7px;letter-spacing:1px;font-weight:700;text-decoration:underline}
.card p{font-size:6px;color:#555;line-height:11px;margin-top:4px;padding:0 10px}
.card .btn{position:absolute;left:23px;top:107px;width:89px;height:23px;background:var(--orange);border-bottom:2px solid var(--teal);font-size:6px;font-weight:700;display:flex;align-items:center;justify-content:center}
.card svg.hex{position:absolute;left:51px;top:18px}
.arrow{top:914px;font-size:11px;font-weight:700;color:var(--ink)}

/* footer */
.footer{left:0;top:1040px;width:708px;height:134px;background:var(--footer);color:var(--white)}
.footer .brand{color:#cfd3d8}
.footer .brand .dot{border-color:#cfd3d8}
.col{top:36px}
.col h4{font-size:9px;font-weight:700;margin-bottom:8px}
.col p{font-size:6px;line-height:13px;color:#cfd3d8;white-space:nowrap}
.social{display:flex;gap:3px}
.social i{width:13px;height:13px;border-radius:50%;background:#cfd3d8;display:block}
.base{left:0;top:1174px;width:708px;height:26px;background:var(--footer-base);color:#cfd3d8;font-size:6px}
</style>
</head>
<body>

<div class="abs topbar">
  <div class="abs item" style="left:362px">
    <svg width="8" height="8" viewBox="0 0 10 10"><path d="M2 1l2 2-1 1.5c.6 1.2 1.3 1.9 2.5 2.5L7 6l2 2-1.3 1.5C4.5 9.3.7 5.5.5 2.3z" fill="var(--teal)"/></svg>
    MEXICO : 52 55 0100 4821
  </div>
  <div class="abs item" style="left:478px">
    <svg width="9" height="7" viewBox="0 0 10 8"><rect x=".5" y=".5" width="9" height="7" fill="none" stroke="var(--teal)"/><path d="M.5 .5l4.5 4 4.5-4" fill="none" stroke="var(--teal)"/></svg>
    EMAIL : info@brindle-passage.org
  </div>
</div>

<header class="abs header">
  <div class="abs brand" style="left:94px;top:11px"><span class="dot"></span><span>Brindle Passage</span></div>
  <nav class="nav">
    <a class="active" href="#" style="left:280px">Home</a>
    <span style="left:324px">:</span>
    <a href="#" style="left:367px">Destinations</a>
    <span style="left:408px">:</span>
    <a href="#" style="left:450px">Universities</a>
    <span style="left:489px">:</span>
    <a href="#" style="left:523px">Hotels</a>
    <span style="left:554px">:</span>
    <a href="#" style="left:594px">Contact Us</a>
  </nav>
</header>

<section class="abs hero" role="img" aria-label="Photo of a red-brick university campus building with lawn and trees under a cloudy sky"></section>
<svg class="abs" style="left:218px;top:152px" width="397" height="106" viewBox="0 0 397 106">
  <polygon points="20,2 394,2 394,48 20,48 2,25" fill="var(--teal)" stroke="var(--orange)" stroke-width="2"/>
  <polygon points="146,66 394,66 394,102 146,102 129,84" fill="var(--teal)" stroke="var(--orange)" stroke-width="2"/>
</svg>
<div class="abs hero-title" style="left:246px;top:160px;font-size:21px">Welcome to The Brindle Passage</div>
<div class="abs hero-title" style="left:371px;top:223px;font-size:15.5px">Hospitality and Culinary Art</div>
<div class="abs cta">CONTACT US</div>
<div class="abs tagline">HOSPITALITY INTERNSHIPS ARE OUR SPECIALTY!</div>

<section class="abs band">
  <h2>Hospitality Internship Program</h2>
  <p>Culinary - F&amp;B - Front Office - Guest - Relations</p>
</section>

<section class="abs contact">
  <p class="abs lead">Hospitality internships are our specialty! Take your paid internship<br>in one of our top international five-star hotels</p>
  <div class="abs field" style="left:134px;top:101px;width:141px">Name</div>
  <div class="abs field" style="left:283px;top:101px;width:141px">E-mail</div>
  <div class="abs field" style="left:433px;top:101px;width:141px">Subject</div>
  <div class="abs field" style="left:134px;top:134px;width:440px;height:40px">Message</div>
  <div class="abs send">Send Message ▸</div>
  <div class="abs resume">Make your resume stand out with an international experience</div>
</section>

<h2 class="abs dest-title">Our Destinations</h2>
<svg class="abs" style="left:0;top:810px" width="204" height="12" viewBox="0 0 204 12">
  <line x1="0" y1="6" x2="194" y2="6" stroke="#b5b5b5" stroke-width="1"/>
  <polygon points="197,1 202,3.5 202,8.5 197,11 192,8.5 192,3.5" fill="#b5b5b5"/>
</svg>

<div class="abs arrow" style="left:86px">←</div>
<div class="abs arrow" style="left:612px">→</div>

<div class="abs card" style="left:120px">
  <svg class="hex" width="32" height="34" viewBox="0 0 32 34"><polygon points="16,0 32,8.5 32,25.5 16,34 0,25.5 0,8.5" fill="var(--teal)"/><circle cx="11" cy="13" r="3" fill="none" stroke="#fff"/><circle cx="21" cy="20" r="3" fill="none" stroke="#fff"/><path d="M11 16v4q0 4 7 3" fill="none" stroke="#fff" stroke-width=".8"/></svg>
  <h3>CHINA</h3>
  <p>Chinese tourists are flocking abroad.<br>With higher earning power</p>
  <div class="btn">MORE INFORMATION</div>
</div>
<div class="abs card" style="left:286px">
  <svg class="hex" width="32" height="34" viewBox="0 0 32 34"><polygon points="16,0 32,8.5 32,25.5 16,34 0,25.5 0,8.5" fill="var(--teal)"/><circle cx="11" cy="13" r="3" fill="none" stroke="#fff"/><circle cx="21" cy="20" r="3" fill="none" stroke="#fff"/><path d="M11 16v4q0 4 7 3" fill="none" stroke="#fff" stroke-width=".8"/></svg>
  <h3>SPAIN</h3>
  <p>Every year millions of tourists travel to<br>Spain, the country has been one..</p>
  <div class="btn">MORE INFORMATION</div>
</div>
<div class="abs card" style="left:453px">
  <svg class="hex" width="32" height="34" viewBox="0 0 32 34"><polygon points="16,0 32,8.5 32,25.5 16,34 0,25.5 0,8.5" fill="var(--teal)"/><circle cx="11" cy="13" r="3" fill="none" stroke="#fff"/><circle cx="21" cy="20" r="3" fill="none" stroke="#fff"/><path d="M11 16v4q0 4 7 3" fill="none" stroke="#fff" stroke-width=".8"/></svg>
  <h3>AUSTRALIA</h3>
  <p>Moving to Australia means running<br>towards opportunities: Australia</p>
  <div class="btn">MORE INFORMATION</div>
</div>

<footer class="abs footer">
  <div class="abs brand" style="left:96px;top:69px"><span class="dot"></span><span>Brindle Passage</span></div>
  <div class="abs col" style="left:268px">
    <h4>FIND US</h4>
    <p>Lorem Ipsum is simply dummy text<br>of the printing and typesetting<br>industry.</p>
  </div>
  <div class="abs col" style="left:397px">
    <h4>GET CONNECTED</h4>
    <p>info@brindle-passage.org<br>+52 55 0100 4821, +1 307-555-0148<br>+33 7 0100 2291, &nbsp;+61 400 555 017</p>
  </div>
  <div class="abs col" style="left:538px">
    <h4>FOLLOW US</h4>
    <div class="social"><i></i><i></i><i></i><i></i><i></i></div>
  </div>
</footer>
<div class="abs base">
  <span class="abs" style="left:95px;top:8px">© Copyright 2018 Brindle-Passage.</span>
  <span class="abs" style="right:96px;top:8px">Privacy Policy &nbsp;| &nbsp;Terms of Use</span>
</div>

</body>
</html>
```